" Assessoria e consultoria de projetos agropecuários com foco em bovinos. DIFERENCIAIS ? Atendimento personalizado; ? Foco em processos; Melhoria continua - metodologia LEAN ? Foco no cliente e na qualidade do serviço; ? Acompanhamento dos resultados gerados pela consultoria; ? Serviço com conhecimento agregado. Atendimento personalizado: A Brota enxerga a necessidade do contato personalizado com o cliente, demonstrando constantemente que a empresa está interessada em ajudá-lo e trazer soluções para seus problemas. ? Foco em processos: Como a maioria das empresas que prestam consultoria na área estão mais voltadas para TÉCNICAS animal, o foco em processos e gestao por processos torna-se um diferencial da Brota. A empresa poderia aproveitar essa vantagem divulgando a importância do gerenciamento eficaz nas fazendas através dos processos agropecuários. ? Foco no cliente e na qualidade do serviço: Através do atendimento personalizado, o consultor da Brota tem a responsabilidade de manter o comprometimento com o cliente e com a qualidade dos serviços entregues. Assim, a empresa cria uma boa relação com os consumidores, fidelizando-os. ? Acompanhamento dos resultados gerados pela consultoria: Além de prestar consultoria, a Empresa auxilia o cliente a implementar as técnicas e soluções, fazendo o acompanhamento de resultados com indicadores. ? Serviço com maior valor agregado: Através da constante busca por conhecimento na área, a qualidade dos projetos entregues será cada vez maior, consequentemente tornando-os mais eficazes e eficientes. "

```html
<!DOCTYPE html>
<html lang="pt-BR">
<head>
<meta charset="UTF-8">
<title>Brota – Pasta institucional</title>
<link rel="stylesheet" href="https://fonts.googleapis.com/css2?family=Montserrat:wght@400;500&display=swap">
<style>
  :root {
    --page-bg: #e9e9ea;
    --navy-deep: #0a1628;
    --navy: #122640;
    --navy-light: #1a3352;
    --emblem-faint: rgba(38, 68, 110, 0.42);
    --green: #3fae5a;
    --green-light: #7fd68e;
    --green-dark: #1f7a38;
    --text-light: #e8ecf1;
    --text-muted: #9aa7b6;
  }
  * { margin: 0; padding: 0; box-sizing: border-box; }
  html, body {
    width: 1200px; height: 1200px; overflow: hidden;
    background: var(--page-bg);
    font-family: "Montserrat", sans-serif;
  }
  .folder-spread {
    position: absolute;
    left: 80px; top: 230px;
    width: 1040px; height: 740px;
    display: flex;
    overflow: hidden;
    box-shadow: 0 20px 50px rgba(0,0,0,0.25);
  }
  .folder-panel {
    position: relative;
    width: 520px; height: 740px;
    background: linear-gradient(160deg, var(--navy-light) 0%, var(--navy) 45%, var(--navy-deep) 100%);
  }
  .folder-panel--back { border-right: 1px solid rgba(0,0,0,0.35); }
  .folder-panel--front { border-left: 1px solid rgba(255,255,255,0.05); }
  .emblem-watermark {
    position: absolute;
    left: 275px; top: 70px;
    width: 490px; height: 490px;
    border-radius: 50%;
    background: radial-gradient(circle, var(--emblem-faint) 0%, rgba(38,68,110,0.28) 70%, rgba(38,68,110,0) 100%);
    z-index: 1;
  }
  .top-band {
    position: absolute; left: 0; top: 0; width: 100%; height: 16px; z-index: 3;
    background: linear-gradient(180deg, var(--green-light) 0%, var(--green) 45%, var(--green-dark) 100%);
  }
  .top-band::after {
    content: ""; position: absolute; left: 0; bottom: -3px; width: 100%; height: 3px;
    background: rgba(0,0,0,0.35);
  }
  .brand {
    position: absolute; z-index: 2;
    display: flex; flex-direction: column; align-items: center;
    text-align: center; color: var(--text-light);
  }
  .brand__mark {
    border-radius: 50%;
    background: var(--text-light);
  }
  .brand__name {
    font-weight: 500; letter-spacing: 0.32em; line-height: 1;
  }
  .brand__tagline {
    font-weight: 400; color: var(--text-muted); letter-spacing: 0.18em;
    text-transform: uppercase; white-space: nowrap;
  }
  .brand--cover { left: 80px; top: 150px; width: 340px; }
  .brand--cover .brand__mark { width: 64px; height: 64px; margin-bottom: 22px; }
  .brand--cover .brand__name { font-size: 56px; margin-right: -0.32em; }
  .brand--cover .brand__tagline { font-size: 11px; margin-top: 10px; }
  .brand--back { left: 60px; top: 455px; width: 170px; }
  .brand--back .brand__mark { width: 30px; height: 30px; margin-bottom: 10px; }
  .brand--back .brand__name { font-size: 26px; margin-right: -0.32em; }
  .brand--back .brand__tagline { font-size: 6px; margin-top: 5px; }
  .contact-list {
    position: absolute; left: 60px; top: 580px; z-index: 2;
    display: grid; grid-template-columns: auto auto; gap: 6px 22px;
    list-style: none; font-size: 9px; color: var(--text-muted);
  }
  .contact-list li { display: flex; align-items: center; gap: 5px; }
  .contact-list svg { width: 9px; height: 9px; fill: var(--text-muted); }
</style>
</head>
<body>
  <main class="folder-spread">
    <section class="folder-panel folder-panel--back">
      <div class="top-band"></div>
      <div class="brand brand--back">
        <div class="brand__mark"></div>
        <div class="brand__name">BROTA</div>
        <div class="brand__tagline">Processos agropecuários</div>
      </div>
      <ul class="contact-list">
        <li><svg viewBox="0 0 10 10"><path d="M2 0.5 L3.6 2.6 L2.8 3.6 Q4 6 6.4 7.2 L7.4 6.4 L9.5 8 L8.3 9.5 Q1 8 0.5 1.7 Z"/></svg>+55 27 3000-1000</li>
        <li><svg viewBox="0 0 10 10"><path d="M2 0.5 L3.6 2.6 L2.8 3.6 Q4 6 6.4 7.2 L7.4 6.4 L9.5 8 L8.3 9.5 Q1 8 0.5 1.7 Z"/></svg>+55 27 3000-2000</li>
        <li><svg viewBox="0 0 10 10"><path d="M0.5 2 H9.5 V8 H0.5 Z M0.5 2 L5 5.5 L9.5 2" fill="none" stroke="#9aa7b6" stroke-width="1"/></svg>contato@brota.agr.br</li>
        <li><svg viewBox="0 0 10 10"><circle cx="5" cy="5" r="4.3" fill="none" stroke="#9aa7b6" stroke-width="1"/><path d="M0.7 5 H9.3 M5 0.7 V9.3" stroke="#9aa7b6" stroke-width="0.8"/></svg>www.brota.agr.br</li>
        <li><svg viewBox="0 0 10 10"><path d="M5 0.5 A3.2 3.2 0 0 1 8.2 3.7 Q8.2 6 5 9.5 Q1.8 6 1.8 3.7 A3.2 3.2 0 0 1 5 0.5 Z"/></svg>Vitória, ES</li>
        <li><svg viewBox="0 0 10 10"><rect x="0.5" y="0.5" width="9" height="9" rx="2.5" fill="none" stroke="#9aa7b6" stroke-width="1"/><circle cx="5" cy="5" r="2" fill="none" stroke="#9aa7b6" stroke-width="1"/></svg>@brota</li>
      </ul>
    </section>
    <section class="folder-panel folder-panel--front">
      <div class="top-band"></div>
      <div class="brand brand--cover">
        <div class="brand__mark"></div>
        <div class="brand__name">BROTA</div>
        <div class="brand__tagline">Processos agropecuários</div>
      </div>
    </section>
    <div class="emblem-watermark" role="img" aria-label="Large faint brand emblem across the spine"></div>
  </main>
</body>
</html>
```